Business Card Design Project

Refresh of logo attached. Require text underneath to be more ledgible, crisper & cleaner.

Overall, staying with same colour scheme need a brighter, crisper, easily readible business card style.

Industry/Entity Type

Business

```html
<!DOCTYPE html>
<html lang="en">
<head>
<meta charset="utf-8">
<title>Veranta Business Card</title>
<link rel="stylesheet" href="https://fonts.googleapis.com/css2?family=Questrial&display=swap">
<style>
  :root {
    --backdrop: #2a2c2f;
    --card: #ffffff;
    --ink: #2b2b2b;
    --blue-light: #2b8fbb;
    --blue-mid: #1a7ea6;
    --blue-dark: #1c4d5f;
    --rule: #555a5e;
    --text-font: "Questrial", "Century Gothic", sans-serif;
  }
  * { margin: 0; padding: 0; box-sizing: border-box; }
  html, body { width: 1200px; height: 858px; overflow: hidden; }
  body {
    background: var(--backdrop);
    font-family: var(--text-font);
    position: relative;
  }
  .card {
    position: absolute;
    top: 280px;
    width: 520px;
    height: 298px;
    background: var(--card);
    overflow: hidden;
  }
  .card--back { left: 60px; }
  .card--front { left: 620px; }
  .card__shapes { position: absolute; inset: 0; width: 100%; height: 100%; }

  .brand { position: absolute; }
  .brand__row { display: flex; align-items: center; gap: 12px; }
  .brand__mark { background: var(--blue-mid); }
  .brand__name { color: var(--ink); letter-spacing: 2px; line-height: 1; }
  .brand__rule { height: 1px; background: var(--rule); margin: 8px 0 5px; }
  .brand__tagline { color: var(--ink); text-transform: uppercase; letter-spacing: 0.3px; white-space: nowrap; }

  .card--back .brand { left: 26px; top: 24px; width: 250px; }
  .card--back .brand__mark { width: 22px; height: 22px; }
  .card--back .brand__name { font-size: 36px; }
  .card--back .brand__tagline { font-size: 8.5px; }

  .card--front .brand { left: 120px; top: 100px; width: 300px; }
  .card--front .brand__mark { width: 28px; height: 28px; }
  .card--front .brand__name { font-size: 48px; }
  .card--front .brand__tagline { font-size: 10px; }

  .contact { position: absolute; left: 26px; top: 118px; list-style: none; }
  .contact__web { color: var(--blue-mid); font-size: 15px; margin-bottom: 7px; }
  .contact__item {
    display: flex; align-items: center; gap: 8px;
    color: var(--ink); font-size: 14px; margin-bottom: 6px;
  }
  .contact__badge {
    width: 18px; height: 18px; border-radius: 50%;
    background: var(--blue-dark); color: #fff;
    font-size: 10px; display: flex; align-items: center; justify-content: center;
  }

  .person { position: absolute; left: 318px; top: 128px; color: #fff; }
  .person__name { font-size: 20px; letter-spacing: 0.3px; white-space: nowrap; }
  .person__title { font-size: 13px; margin-top: 4px; white-space: nowrap; }
</style>
</head>
<body>

  <section class="card card--back" aria-label="Business card, contact side">
    <svg class="card__shapes" viewBox="0 0 520 298" aria-hidden="true">
      <polygon points="300,108 520,108 520,210 312,210" fill="var(--blue-light)"/>
      <polygon points="236,216 520,216 520,298 150,298" fill="var(--blue-dark)"/>
    </svg>

    <div class="brand">
      <div class="brand__row">
        <span class="brand__mark"></span>
        <span class="brand__name">VERANTA</span>
      </div>
      <div class="brand__rule"></div>
      <div class="brand__tagline">Veranta Institute of Estate Guidance</div>
    </div>

    <ul class="contact">
      <li class="contact__web">www.veranta.example</li>
      <li class="contact__item"><span class="contact__badge">T</span>(555) 014 2287</li>
      <li class="contact__item"><span class="contact__badge">M</span>(555) 019 4410</li>
      <li class="contact__item"><span class="contact__badge">E</span>daniel@veranta.example</li>
    </ul>

    <div class="person">
      <div class="person__name">Daniel R. Ashworth</div>
      <div class="person__title">Certified Executor Advisor</div>
    </div>
  </section>

  <section class="card card--front" aria-label="Business card, brand side">
    <div class="brand">
      <div class="brand__row">
        <span class="brand__mark"></span>
        <span class="brand__name">VERANTA</span>
      </div>
      <div class="brand__rule"></div>
      <div class="brand__tagline">Veranta Institute of Estate Guidance</div>
    </div>
  </section>

</body>
</html>
```